Business Card Design Project

We need a business card for a chiropractic and rehabilitation center. We already have a logo and need the card to follow the color and feel of the logo.

Target Market(s)

adults 30-55 that have some ache or pain that is interfering with their life, so much as they are ready to do something about it.

Industry/Entity Type

Business

```html
<!DOCTYPE html>
<html lang="en">
<head>
<meta charset="utf-8">
<title>Vitalis Wellness Center – Business Card</title>
<link rel="stylesheet" href="https://fonts.googleapis.com/css2?family=Roboto:wght@400&display=swap">
<style>
  :root {
    --orange: #f7931e;
    --red: #be1e2d;
    --slate: #58595b;
    --paper: #ffffff;
    --ink: #414042;
    --backdrop: #d6d6d6;
  }
  * { margin: 0; padding: 0; box-sizing: border-box; }
  html, body {
    width: 1067px;
    height: 1200px;
    overflow: hidden;
    background: var(--backdrop);
  }
  .canvas {
    position: relative;
    width: 1067px;
    height: 1200px;
    font-family: "Roboto", sans-serif;
    font-weight: 400;
  }
  .card {
    position: absolute;
    left: 183px;
    width: 700px;
    height: 400px;
    overflow: hidden;
    box-shadow: 0 6px 18px rgba(0,0,0,0.18);
  }
  .card--front { top: 110px; }
  .card--back { top: 650px; background: var(--paper); }
  .card__bands {
    position: absolute;
    inset: 0;
    width: 100%;
    height: 100%;
  }
  .business-name {
    position: absolute;
    white-space: nowrap;
    line-height: 1;
  }
  .card--front .business-name {
    left: 250px;
    top: 178px;
    font-size: 38px;
    color: var(--paper);
  }
  .front-url {
    position: absolute;
    left: 330px;
    top: 282px;
    font-size: 17px;
    color: var(--paper);
    letter-spacing: 0.3px;
  }
  .card--back .business-name {
    left: 38px;
    top: 140px;
    font-size: 28px;
    color: var(--slate);
  }
  .address {
    position: absolute;
    left: 38px;
    top: 232px;
    font-size: 13.5px;
    color: var(--ink);
    line-height: 1.45;
  }
  .address__row { display: flex; align-items: center; gap: 7px; }
  .address__row--indent { padding-left: 21px; }
  .address__web { color: var(--orange); font-size: 15px; }
  .contact {
    position: absolute;
    right: 36px;
    top: 132px;
    font-size: 13.5px;
    color: var(--ink);
    text-align: right;
    line-height: 1.55;
  }
  .contact__name { color: var(--red); font-size: 17px; }
  .contact__row { display: flex; justify-content: flex-end; align-items: center; gap: 7px; }
  .icon { width: 14px; height: 14px; flex: none; }
  .icon path, .icon circle, .icon rect { fill: none; stroke: var(--slate); stroke-width: 1.6; }
  .icon .solid { fill: var(--slate); stroke: none; }
</style>
</head>
<body>
<main class="canvas">

  <section class="card card--front" aria-label="Card front">
    <svg class="card__bands" viewBox="0 0 700 400" preserveAspectRatio="none" aria-hidden="true">
      <rect width="700" height="400" fill="var(--slate)"/>
      <polygon points="0,0 365,0 120,400 0,400" fill="var(--orange)"/>
      <polygon points="365,0 560,0 315,400 120,400" fill="var(--red)"/>
    </svg>
    <div class="business-name">Vitalis Wellness Center</div>
    <div class="front-url">www.vitalis-wellness.com</div>
  </section>

  <section class="card card--back" aria-label="Card back">
    <svg class="card__bands" viewBox="0 0 700 400" preserveAspectRatio="none" aria-hidden="true">
      <polygon points="0,345 420,345 386,400 0,400" fill="var(--slate)"/>
      <polygon points="420,345 560,345 526,400 386,400" fill="var(--red)"/>
      <polygon points="560,345 700,345 700,400 526,400" fill="var(--orange)"/>
    </svg>

    <div class="business-name">Vitalis Wellness Center</div>

    <div class="address">
      <div class="address__row">
        <svg class="icon" viewBox="0 0 14 14" aria-hidden="true">
          <circle cx="7" cy="7" r="5.8"/>
          <path d="M1.2 7h11.6M7 1.2c-2.4 3-2.4 8.6 0 11.6M7 1.2c2.4 3 2.4 8.6 0 11.6"/>
        </svg>
        <span class="address__web">www.vitalis-wellness.com</span>
      </div>
      <div class="address__row">
        <svg class="icon" viewBox="0 0 14 14" aria-hidden="true">
          <path class="solid" d="M7 1 0.5 7h2v6h3.5V9h2v4h3.5V7h2z"/>
        </svg>
        <span>2140 Cedar Ridge Dr, Ste 101</span>
      </div>
      <div class="address__row address__row--indent">Austin TX 78745</div>
    </div>

    <div class="contact">
      <div class="contact__name">Marcus Reed, DC</div>
      <div class="contact__row">
        <span>drreed@vitalis-wellness.com</span>
        <svg class="icon" viewBox="0 0 14 14" aria-hidden="true">
          <rect x="1" y="3" width="12" height="8"/>
          <path d="M1 3l6 4.5L13 3"/>
        </svg>
      </div>
      <div class="contact__row">
        <span>512.555.0148</span>
        <svg class="icon" viewBox="0 0 14 14" aria-hidden="true">
          <path class="solid" d="M3.2 1.2 5.3 3.6 4.2 5.3c.8 1.8 2.3 3.3 4.1 4.1l1.7-1.1 2.4 2.1-1.2 2.2C6.2 12.4 1.6 7.8 1 2.4z"/>
        </svg>
      </div>
    </div>
  </section>

</main>
</body>
</html>
```